Hey There Pinecrest....a heavily based video and picture gallery style website.

Would like a multipage website for videos and pictures. For example, one page/category will be Events. I would like that page to be a thumbnail gallery where the user would click on a thumbnail and the video will play over/hover the the thumbnail page(not go to another page). So when the user closes the player, they are still on the events page. On each page, would like a navigation bar to be able to go to the other pages/categories. And I would like it this way for the other categories as well (people, places, meet the vendors, pictures....) Please view my current website for all pages needed. I only submitted a fraction of images. How should i send the videos? Please contact if questions.
My current website is at www.heytherepinecrest.example

Target Market(s)

male/female, 30-70+ years old

Industry/Entity Type

Entertainment

Coding

Coded - Design and coding required

Number of Pages Required

5+ page

Font styles to use
Sans Serif

Colors
0393ce
00a990
f04a51
f68d4e

Requirements
Must have
• social media links. the video player must play/hover over the current page rather than going to another page. my logo. a calendar page where I can add events to it. a text area under videos for description, photo gallery for each category, the ability to copy a page to use as a template to add more videos and pictures in the future, contact page, the ability to add google ads, affiliate advertising.

```html
<!DOCTYPE html>
<html lang="en">
<head>
<meta charset="utf-8">
<title>Hey There Pinecrest</title>
<link href="https://fonts.googleapis.com/css2?family=Lato:wght@300;400;700;900&display=swap" rel="stylesheet">
<style>
:root{
  --blue:#0393ce;
  --teal:#00a990;
  --red:#f04a51;
  --orange:#f68d4e;
  --ink:#2c2c2c;
  --muted:#7d7d7d;
  --line:#dcdcdc;
  --footer:#111d25;
  --footer-2:#22353f;
  --play:#e0262d;
  --subscribe:#0e7d5f;
}
*{box-sizing:border-box;margin:0;padding:0}
html,body{width:1200px;height:3600px;overflow:hidden}
body{position:relative;font-family:'Lato',Arial,sans-serif;color:var(--ink);background:#fff}
.abs{position:absolute}

/* header */
.site-header{position:absolute;left:0;top:0;width:1200px;height:145px;background:#fff;border-top:5px solid var(--teal);z-index:3}
.brand{position:absolute;left:100px;top:18px;width:200px;height:200px;border-radius:50%;background:#fff;display:flex;align-items:center;justify-content:center;text-align:center;z-index:4}
.brand-name{font-weight:900;font-size:25px;line-height:1.1;color:#1f5f8b;text-transform:uppercase;margin-top:-40px}
.search{position:absolute;left:630px;top:30px;width:300px;height:36px;border:1px solid var(--line);border-radius:3px;font-size:13px;color:#aaa;padding:9px 12px}
.social{position:absolute;top:30px;width:34px;height:34px;border-radius:50%}
.main-nav{position:absolute;top:102px;left:0;width:1200px;font-size:14px;text-transform:uppercase;color:#333}
.main-nav span{position:absolute;top:0}
.main-nav .active{color:var(--blue)}
.main-nav .active::before{content:"";position:absolute;left:-4px;right:-4px;top:-12px;height:3px;background:var(--blue)}
.caret{position:static!important;font-size:9px}

/* imagery placeholders */
.photo{position:absolute;left:0;top:0;width:100%}

/* hero */
.hero{position:absolute;left:0;top:145px;width:1200px;height:580px;overflow:hidden}
.hero .photo{height:100%;background:
  radial-gradient(ellipse 190px 110px at 250px 400px,rgba(40,35,30,.75),transparent 70%),
  radial-gradient(ellipse 150px 120px at 960px 390px,rgba(40,35,30,.75),transparent 70%),
  radial-gradient(ellipse 420px 90px at 600px 300px,rgba(40,70,30,.8),transparent 70%),
  radial-gradient(ellipse 500px 160px at 900px 60px,rgba(225,232,240,.9),transparent 70%),
  linear-gradient(180deg,#5f7896 0%,#8aa0b8 22%,#aab7b0 40%,#5f7a3c 55%,#7b8f3f 72%,#4b6328 100%)}
.hero-title{position:absolute;top:185px;width:100%;text-align:center;color:#fff;font-weight:900;font-size:50px;letter-spacing:.5px;text-shadow:0 2px 8px rgba(0,0,0,.35)}
.hero-sub{position:absolute;top:275px;width:100%;text-align:center;color:#fff;font-size:14px;text-shadow:0 1px 4px rgba(0,0,0,.5)}
.hero-wave{position:absolute;left:0;bottom:0;width:1200px;height:110px}

.play{position:absolute;width:54px;height:54px;border-radius:50%;background:var(--play);transform:translate(-50%,-50%);box-shadow:0 0 0 4px rgba(255,255,255,.35)}
.play::after{content:"";position:absolute;left:21px;top:16px;border-left:17px solid #fff;border-top:11px solid transparent;border-bottom:11px solid transparent}
.play.sm{width:40px;height:40px}
.play.sm::after{left:16px;top:12px;border-left:12px solid #fff;border-top:8px solid transparent;border-bottom:8px solid transparent}

/* sections */
.section-title{position:absolute;left:0;width:1200px;text-align:center;font-size:30px;font-weight:400;text-transform:uppercase}
.title-rule{position:absolute;height:1px}
.welcome-text{position:absolute;left:330px;top:846px;width:540px;text-align:center;font-size:13px;line-height:26px;color:var(--muted)}
.feature{position:absolute;top:935px;width:490px;height:350px;overflow:hidden}
.feature .photo{height:295px}
.feature .caption{position:absolute;left:0;bottom:0;width:100%;height:55px;background:linear-gradient(90deg,var(--blue),#0aa6c7);color:#fff;font-size:16px;text-transform:uppercase;text-align:center;line-height:55px}

.band-categories{position:absolute;left:0;top:1365px;width:1200px;height:735px;background:linear-gradient(180deg,var(--teal),var(--blue))}
.band-uploads{position:absolute;left:0;top:2100px;width:1200px;height:495px;background:linear-gradient(180deg,var(--orange),var(--red))}
.band .section-title{color:#fff}

.tile{position:absolute;width:242px;height:255px;background:#fff;overflow:hidden}
.tile .photo{height:200px}
.tile svg{position:absolute;left:0;top:155px;width:242px;height:100px}
.tile .label{position:absolute;left:0;bottom:16px;width:100%;text-align:center;font-size:14px;text-transform:uppercase;color:#333}
.quote-text{position:absolute;left:40px;top:8px;color:#fff;font-size:11px;font-weight:700;line-height:16px}

.soon{position:absolute;top:2738px;width:320px;height:265px}
.soon .photo{height:217px}
.soon .caption{position:absolute;left:0;bottom:0;width:100%;height:48px;color:#fff;font-size:15px;text-align:center;line-height:48px}

/* footer */
.site-footer{position:absolute;left:0;top:3060px;width:1200px;height:540px}
.footer-bg{position:absolute;left:0;top:0;width:1200px;height:540px}
.footer-brand{position:absolute;left:98px;top:255px;width:180px;color:#fff;font-weight:900;font-size:24px;line-height:1.1;text-transform:uppercase}
.footer-head{position:absolute;top:212px;color:#fff;font-size:16px;font-weight:400;text-transform:uppercase}
.contact-line{position:absolute;left:335px;color:#fff;font-size:13px;line-height:20px;display:flex;gap:14px}
.contact-line svg{flex:none;margin-top:3px}
.news-text{position:absolute;left:588px;top:248px;width:220px;color:#fff;font-size:12px;line-height:20px}
.news-input{position:absolute;left:588px;top:292px;width:217px;height:36px;background:#fff;font-size:12px;color:#999;padding:10px}
.news-btn{position:absolute;left:588px;top:338px;width:118px;height:36px;background:var(--subscribe);color:#fff;font-size:12px;text-transform:uppercase;text-align:center;line-height:36px}
.affiliate{position:absolute;border-radius:2px;box-shadow:0 1px 3px rgba(0,0,0,.4)}
.footer-rule{position:absolute;left:98px;top:450px;width:1002px;height:1px;background:rgba(255,255,255,.3)}
.copyright{position:absolute;top:495px;width:1200px;text-align:center;color:#fff;font-size:12px}
</style>
</head>
<body>

<header class="site-header">
  <div class="search">Search...</div>
  <div class="social" style="left:950px;background:#3b5998"></div>
  <div class="social" style="left:990px;background:#1da1f2"></div>
  <div class="social" style="left:1030px;background:#e52d27"></div>
  <div class="social" style="left:1070px;background:#555"></div>
  <nav class="main-nav">
    <span class="active" style="left:432px">Home</span>
    <span style="left:548px">Videos <span class="caret">&#9662;</span></span>
    <span style="left:688px">Photo Gallery <span class="caret">&#9662;</span></span>
    <span style="left:885px">Calendar</span>
    <span style="left:1032px">Contact</span>
  </nav>
</header>
<div class="brand"><div class="brand-name">Hey There<br>Pinecrest</div></div>

<section class="hero">
  <div class="photo" role="img" aria-label="Savanna landscape with two elephants, acacia trees and a cloudy sky"></div>
  <h1 class="hero-title">HEY THERE PINECREST</h1>
  <p class="hero-sub">Sed ut perspiciatis unde omnis iste natus error sit voluptatem accusantium</p>
  <div class="play" style="left:600px;top:350px"></div>
  <svg class="hero-wave" viewBox="0 0 1200 110" preserveAspectRatio="none">
    <path d="M0 80 C300 20 700 20 1200 40 L1200 110 L0 110 Z" fill="var(--blue)"/>
    <path d="M0 95 C300 35 700 35 1200 55 L1200 110 L0 110 Z" fill="#fff"/>
  </svg>
</section>

<h2 class="section-title" style="top:795px">Welcome to Hey There Pinecrest</h2>
<p class="welcome-text">Excepteur cupidatat blacks are not excepteur, is soothing to the soul, that is, they deserted the general duties of those wre not excepteur, is soothe are to blame for your trouble</p>

<div class="feature" style="left:98px">
  <div class="photo" role="img" aria-label="Collage of world landmarks and a city skyline under a blue sky" style="background:
    radial-gradient(ellipse 60px 130px at 95px 190px,rgba(70,150,130,.85),transparent 75%),
    radial-gradient(ellipse 150px 60px at 380px 230px,rgba(150,150,150,.8),transparent 75%),
    radial-gradient(ellipse 220px 40px at 245px 270px,rgba(120,100,80,.7),transparent 75%),
    radial-gradient(ellipse 160px 80px at 380px 60px,rgba(255,255,255,.95),transparent 70%),
    linear-gradient(180deg,#5e9fd6 0%,#a9cdea 40%,#dfe8ee 65%,#b9b2a4 100%)"></div>
  <div class="play" style="left:245px;top:148px"></div>
  <div class="caption">Guest Photo Montage</div>
</div>
<div class="feature" style="left:610px">
  <div class="photo" role="img" aria-label="Lush community garden with lawn, flower beds and willow trees" style="background:
    radial-gradient(ellipse 230px 70px at 250px 230px,rgba(150,205,60,.95),transparent 75%),
    radial-gradient(ellipse 70px 40px at 90px 200px,rgba(200,60,50,.75),transparent 75%),
    radial-gradient(ellipse 120px 150px at 400px 90px,rgba(150,190,90,.85),transparent 75%),
    radial-gradient(ellipse 110px 120px at 90px 70px,rgba(25,50,20,.9),transparent 75%),
    linear-gradient(180deg,#2f4f22 0%,#456b2d 40%,#6f9b3a 70%,#8bb83d 100%)"></div>
  <div class="play" style="left:245px;top:148px"></div>
  <div class="caption">Ridgeview Community Garden</div>
</div>

<section class="band band-categories">
  <div class="title-rule" style="left:218px;top:87px;width:270px;background:rgba(255,255,255,.5)"></div>
  <div class="title-rule" style="left:712px;top:87px;width:270px;background:rgba(255,255,255,.5)"></div>
  <h2 class="section-title" style="top:68px">Categories</h2>
</section>

<div class="tile" style="left:98px;top:1510px"><div class="photo" role="img" aria-label="Figure on a hill under a starry night sky" style="background:radial-gradient(ellipse 90px 60px at 170px 60px,rgba(200,170,220,.55),transparent 75%),radial-gradient(ellipse 140px 50px at 60px 190px,rgba(20,20,40,.9),transparent 75%),linear-gradient(180deg,#1e2a5a,#4b4a85 50%,#8a6a9e)"></div><div class="play sm" style="left:121px;top:95px"></div><svg viewBox="0 0 242 100" preserveAspectRatio="none"><path d="M0 100 L0 40 Q121 -30 242 40 L242 100 Z" fill="#fff" stroke="var(--teal)" stroke-width="3"/></svg><div class="label">People</div></div>
<div class="tile" style="left:352px;top:1510px"><div class="photo" role="img" aria-label="Group of friends laughing together outdoors" style="background:radial-gradient(ellipse 50px 60px at 50px 90px,rgba(210,160,120,.9),transparent 75%),radial-gradient(ellipse 50px 60px at 190px 80px,rgba(200,150,110,.9),transparent 75%),radial-gradient(ellipse 80px 50px at 120px 170px,rgba(80,70,70,.7),transparent 75%),linear-gradient(180deg,#e9e2d6,#c9a284 55%,#8a6a55)"></div><div class="play sm" style="left:121px;top:95px"></div><svg viewBox="0 0 242 100" preserveAspectRatio="none"><path d="M0 100 L0 40 Q121 -30 242 40 L242 100 Z" fill="#fff" stroke="var(--teal)" stroke-width="3"/></svg><div class="label">Events</div></div>
<div class="tile" style="left:605px;top:1510px"><div class="photo" role="img" aria-label="Vendor serving a customer at a shop counter" style="background:radial-gradient(ellipse 60px 50px at 90px 140px,rgba(200,40,40,.75),transparent 75%),radial-gradient(ellipse 60px 90px at 200px 110px,rgba(70,90,130,.8),transparent 75%),linear-gradient(180deg,#e4e7ea,#b2bac4 50%,#7e8a99)"></div><div class="play sm" style="left:121px;top:95px"></div><svg viewBox="0 0 242 100" preserveAspectRatio="none"><path d="M0 100 L0 40 Q121 -30 242 40 L242 100 Z" fill="#fff" stroke="var(--teal)" stroke-width="3"/></svg><div class="label">Meet the Vendors</div></div>
<div class="tile" style="left:858px;top:1510px"><div class="photo" role="img" aria-label="Giant panda among green leaves" style="background:radial-gradient(ellipse 80px 80px at 125px 100px,rgba(245,245,240,.95),transparent 75%),radial-gradient(ellipse 60px 40px at 125px 180px,rgba(30,30,30,.8),transparent 75%),linear-gradient(180deg,#3f5a2a,#6f8b4a 50%,#4a5e33)"></div><div class="play sm" style="left:121px;top:95px"></div><svg viewBox="0 0 242 100" preserveAspectRatio="none"><path d="M0 100 L0 40 Q121 -30 242 40 L242 100 Z" fill="#fff" stroke="var(--teal)" stroke-width="3"/></svg><div class="label">Scenic Videos</div></div>

<div class="tile" style="left:98px;top:1775px"><div class="photo" role="img" aria-label="Three performers smiling together" style="background:radial-gradient(ellipse 45px 60px at 40px 80px,rgba(200,140,110,.9),transparent 75%),radial-gradient(ellipse 45px 60px at 200px 90px,rgba(120,80,60,.9),transparent 75%),radial-gradient(ellipse 60px 50px at 110px 170px,rgba(210,70,110,.75),transparent 75%),linear-gradient(180deg,#5a3a45,#9a6060 50%,#6a3a45)"></div><div class="play sm" style="left:121px;top:95px"></div><svg viewBox="0 0 242 100" preserveAspectRatio="none"><path d="M0 100 L0 40 Q121 -30 242 40 L242 100 Z" fill="#fff" stroke="var(--teal)" stroke-width="3"/></svg><div class="label">Performances</div></div>
<div class="tile" style="left:352px;top:1775px"><div class="photo" role="img" aria-label="Open water seen from a wooden dock" style="background:radial-gradient(ellipse 90px 50px at 190px 170px,rgba(140,100,60,.9),transparent 75%),linear-gradient(180deg,#8fb0c2 0%,#b9cbd4 18%,#2c6580 24%,#1f4b5e 65%,#173a48)"></div><div class="play sm" style="left:121px;top:95px"></div><svg viewBox="0 0 242 100" preserveAspectRatio="none"><path d="M0 100 L0 40 Q121 -30 242 40 L242 100 Z" fill="#fff" stroke="var(--teal)" stroke-width="3"/></svg><div class="label">The Lighter Side</div></div>
<div class="tile" style="left:605px;top:1775px"><div class="photo" role="img" aria-label="Quote card over a warm blurred background" style="background:radial-gradient(ellipse 60px 70px at 70px 150px,rgba(170,130,80,.8),transparent 75%),radial-gradient(ellipse 80px 60px at 190px 110px,rgba(90,110,130,.6),transparent 75%),linear-gradient(180deg,#1f1f1f,#4a3a2a 60%,#6b5233)"></div><div class="quote-text">LIFE IS 10% WHAT HAPPENS<br>...AND 90% HOW I REACT</div><div class="play sm" style="left:121px;top:95px"></div><svg viewBox="0 0 242 100" preserveAspectRatio="none"><path d="M0 100 L0 40 Q121 -30 242 40 L242 100 Z" fill="#fff" stroke="var(--teal)" stroke-width="3"/></svg><div class="label">Quote of the Day</div></div>
<div class="tile" style="left:858px;top:1775px"><div class="photo" role="img" aria-label="Deer standing in a misty field" style="background:radial-gradient(ellipse 60px 60px at 140px 110px,rgba(150,120,95,.8),transparent 75%),linear-gradient(180deg,#a4a294,#b9b3a3 55%,#9a9480)"></div><div class="play sm" style="left:121px;top:95px"></div><svg viewBox="0 0 242 100" preserveAspectRatio="none"><path d="M0 100 L0 40 Q121 -30 242 40 L242 100 Z" fill="#fff" stroke="var(--teal)" stroke-width="3"/></svg><div class="label">Wildlife</div></div>

<section class="band band-uploads">
  <div class="title-rule" style="left:218px;top:92px;width:230px;background:rgba(255,255,255,.5)"></div>
  <div class="title-rule" style="left:752px;top:92px;width:230px;background:rgba(255,255,255,.5)"></div>
  <h2 class="section-title" style="top:73px">Recent Uploads</h2>
</section>

<div class="tile" style="left:98px;top:2255px"><div class="photo" role="img" aria-label="Smiling woman at an outdoor market stall" style="background:radial-gradient(ellipse 70px 90px at 170px 90px,rgba(120,80,55,.9),transparent 75%),radial-gradient(ellipse 60px 50px at 150px 170px,rgba(60,150,170,.75),transparent 75%),linear-gradient(180deg,#d7dde0,#9aa4a8 50%,#7a6a5e)"></div><div class="play sm" style="left:121px;top:95px"></div><svg viewBox="0 0 242 100" preserveAspectRatio="none"><path d="M0 100 L0 40 Q121 -30 242 40 L242 100 Z" fill="#fff" stroke="var(--teal)" stroke-width="3"/></svg><div class="label">Kelp Cove</div></div>
<div class="tile" style="left:352px;top:2255px"><div class="photo" role="img" aria-label="Chalkboard sign at a sauce vendor booth" style="background:radial-gradient(ellipse 90px 40px at 110px 40px,rgba(240,230,220,.35),transparent 75%),radial-gradient(ellipse 90px 40px at 110px 110px,rgba(230,80,80,.45),transparent 75%),radial-gradient(ellipse 70px 30px at 110px 170px,rgba(200,170,60,.5),transparent 75%),linear-gradient(180deg,#2a2a2a,#3e3534)"></div><div class="play sm" style="left:121px;top:95px"></div><svg viewBox="0 0 242 100" preserveAspectRatio="none"><path d="M0 100 L0 40 Q121 -30 242 40 L242 100 Z" fill="#fff" stroke="var(--teal)" stroke-width="3"/></svg><div class="label">Smoky Hill BBQ Sauce</div></div>
<div class="tile" style="left:605px;top:2255px"><div class="photo" role="img" aria-label="Musicians playing under magenta stage light" style="background:radial-gradient(ellipse 60px 70px at 60px 100px,rgba(230,80,150,.8),transparent 75%),radial-gradient(ellipse 60px 70px at 190px 90px,rgba(200,50,120,.7),transparent 75%),linear-gradient(180deg,#2a0a20,#6a1a4a 55%,#3a0f2a)"></div><div class="play sm" style="left:121px;top:95px"></div><svg viewBox="0 0 242 100" preserveAspectRatio="none"><path d="M0 100 L0 40 Q121 -30 242 40 L242 100 Z" fill="#fff" stroke="var(--teal)" stroke-width="3"/></svg><div class="label">Marco &amp; Jim</div></div>
<div class="tile" style="left:858px;top:2255px"><div class="photo" role="img" aria-label="Hand-painted berry farm banner" style="background:radial-gradient(ellipse 100px 35px at 120px 55px,rgba(245,240,250,.55),transparent 75%),radial-gradient(ellipse 100px 35px at 120px 120px,rgba(245,240,250,.5),transparent 75%),radial-gradient(ellipse 40px 60px at 20px 60px,rgba(220,60,70,.8),transparent 75%),linear-gradient(180deg,#8c6fb0,#6a4f8a)"></div><div class="play sm" style="left:121px;top:95px"></div><svg viewBox="0 0 242 100" preserveAspectRatio="none"><path d="M0 100 L0 40 Q121 -30 242 40 L242 100 Z" fill="#fff" stroke="var(--teal)" stroke-width="3"/></svg><div class="label">Dale's Berries</div></div>

<div class="title-rule" style="left:218px;top:2688px;width:245px;background:var(--line)"></div>
<div class="title-rule" style="left:737px;top:2688px;width:245px;background:var(--line)"></div>
<h2 class="section-title" style="top:2668px">Coming Soon</h2>

<div class="soon" style="left:100px"><div class="photo" role="img" aria-label="Vendor at a candy booth with a green backdrop" style="background:radial-gradient(ellipse 110px 90px at 230px 60px,rgba(30,150,70,.95),transparent 75%),radial-gradient(ellipse 80px 60px at 150px 130px,rgba(190,140,90,.8),transparent 75%),radial-gradient(ellipse 180px 40px at 160px 200px,rgba(40,45,60,.9),transparent 75%),linear-gradient(180deg,#cfd4d0,#7b8a80 50%,#3a3f48)"></div><div class="play sm" style="left:160px;top:108px"></div><div class="caption" style="background:var(--teal)">Toffee Kitchen</div></div>
<div class="soon" style="left:447px"><div class="photo" role="img" aria-label="People flying kites on a grassy field" style="background:radial-gradient(ellipse 40px 30px at 60px 50px,rgba(220,110,40,.8),transparent 75%),radial-gradient(ellipse 160px 30px at 160px 150px,rgba(60,70,90,.6),transparent 75%),linear-gradient(180deg,#a9c0cc 0%,#c9d6da 55%,#6f8f4a 68%,#5d7f3a)"></div><div class="play sm" style="left:160px;top:108px"></div><div class="caption" style="background:var(--blue)">Through My Lens Photography</div></div>
<div class="soon" style="left:780px"><div class="photo" role="img" aria-label="Antique sewing machine with colourful fabrics" style="background:radial-gradient(ellipse 90px 40px at 110px 40px,rgba(220,170,60,.8),transparent 75%),radial-gradient(ellipse 80px 60px at 230px 140px,rgba(60,50,45,.9),transparent 75%),radial-gradient(ellipse 60px 50px at 60px 150px,rgba(160,120,150,.7),transparent 75%),linear-gradient(180deg,#6a4a3a,#4a352a 60%,#2f2420)"></div><div class="play sm" style="left:160px;top:108px"></div><div class="caption" style="background:var(--orange)">Cap &amp; Brim Shop</div></div>

<footer class="site-footer">
  <svg class="footer-bg" viewBox="0 0 1200 540" preserveAspectRatio="none">
    <defs>
      <linearGradient id="footerShade" x1="0" y1="0" x2="0" y2="1"><stop offset="0" stop-color="var(--footer-2)"/><stop offset="1" stop-color="var(--footer)"/></linearGradient>
      <radialGradient id="footerGlow" cx=".5" cy=".35" r=".6"><stop offset="0" stop-color="#3a5563" stop-opacity=".55"/><stop offset="1" stop-color="#3a5563" stop-opacity="0"/></radialGradient>
    </defs>
    <path d="M0 20 C300 90 800 100 1200 20 L1200 540 L0 540 Z" fill="url(#footerShade)"/>
    <path d="M0 20 C300 90 800 100 1200 20 L1200 540 L0 540 Z" fill="url(#footerGlow)"/>
    <path d="M0 45 C350 110 850 110 1200 35" fill="none" stroke="var(--blue)" stroke-width="6"/>
    <path d="M0 28 C350 98 850 98 1200 24 L1200 0 L0 0 Z" fill="#fff"/>
  </svg>
  <div class="footer-brand">Hey There<br>Pinecrest</div>

  <h3 class="footer-head" style="left:335px">Contact Us</h3>
  <div class="contact-line" style="top:258px"><svg width="14" height="14" viewBox="0 0 14 14"><path d="M7 1 L1 6 H3 V13 H6 V9 H8 V13 H11 V6 H13 Z" fill="#fff"/></svg><span>2280 Cedar Bluff Rd. | Pinecrest<br>WA 98000</span></div>
  <div class="contact-line" style="top:318px"><svg width="12" height="16" viewBox="0 0 12 16"><rect x="1" y="0" width="10" height="16" rx="2" fill="#fff"/><rect x="3" y="2" width="6" height="10" fill="var(--footer)"/></svg><span>Call Us : (555) - 014 - 2277</span></div>
  <div class="contact-line" style="top:358px"><svg width="16" height="12" viewBox="0 0 16 12"><rect x="0.5" y="0.5" width="15" height="11" fill="none" stroke="#fff"/><path d="M1 1 L8 7 L15 1" fill="none" stroke="#fff"/></svg><span>hello@heytherepinecrest.example</span></div>

  <h3 class="footer-head" style="left:588px">Sign Up Newsletter</h3>
  <p class="news-text">Ut enimad minima veniam, quis nostrum aliquid cinima venomeeps..</p>
  <div class="news-input">Enter Email...</div>
  <div class="news-btn">Subscribe</div>

  <h3 class="footer-head" style="left:915px;top:220px">Affiliate Links</h3>
  <div class="affiliate" style="left:898px;top:280px;width:64px;height:40px;background:#d32a2a"></div>
  <div class="affiliate" style="left:978px;top:284px;width:92px;height:24px;background:#fff;border-bottom:6px solid #111"></div>
  <div class="affiliate" style="left:868px;top:340px;width:234px;height:32px;background:#fff;border:2px solid #b9c1c6"></div>

  <div class="footer-rule"></div>
  <p class="copyright">&copy; copyright 2017 &nbsp;Hey There Pinecrest . All rights reserved.</p>
</footer>

</body>
</html>
```